We were billed for this because the project timed out. Please give me another designed to open this back up. I was not happy with the last designs (that I was charged for).
we are also using the logo with Bringing Clear Water to Every Pool
Also want to utilize Where Healthy Water is our Commitment.

Contact Information for Business Card

Marlowe Crest Group Inc

```html
<!DOCTYPE html>
<html lang="en">
<head>
<meta charset="utf-8">
<title>Marlowe Crest Group – Business Cards</title>
<link rel="stylesheet" href="https://fonts.googleapis.com/css2?family=Michroma&family=Montserrat:wght@500;700&display=swap">
<style>
  :root {
    --bg: #2b2d30;
    --water-light: #4f9fe6;
    --water-mid: #2f83d6;
    --water-deep: #1f6cc4;
    --ink: #3a3f45;
    --brand-blue: #1f6cc4;
    --paper: #ffffff;
    --tagline: #bfe0ff;
  }
  * { margin: 0; padding: 0; box-sizing: border-box; }
  html, body { width: 1200px; height: 1200px; overflow: hidden; }
  body { background: var(--bg); position: relative; font-family: "Montserrat", sans-serif; }

  .card { position: absolute; overflow: hidden; box-shadow: 0 18px 40px rgba(0,0,0,.45); }

  .water {
    position: absolute; inset: 0;
    background: linear-gradient(180deg, var(--water-light) 0%, var(--water-mid) 55%, var(--water-deep) 100%);
  }

  /* Front card */
  .card-front { left: 490px; top: 160px; width: 590px; height: 330px; }
  .front-brand {
    position: absolute; inset: 0;
    display: flex; flex-direction: column; align-items: center; justify-content: center;
    text-align: center; color: var(--paper);
  }
  .front-brand .mark { width: 26px; height: 26px; background: var(--paper); margin-bottom: 16px; }
  .front-brand .company { font-family: "Michroma", sans-serif; font-size: 24px; letter-spacing: 1px; }
  .front-brand .tagline { font-family: "Michroma", sans-serif; font-size: 10.5px; letter-spacing: 1.4px; color: var(--tagline); margin-top: 8px; text-transform: uppercase; }

  /* Back card */
  .card-back { left: 130px; top: 470px; width: 360px; height: 600px; }
  .back-header {
    position: absolute; left: 0; top: 0; width: 100%; height: 140px;
    background: var(--paper); border-bottom-right-radius: 60px;
    display: flex; flex-direction: column; align-items: center; justify-content: center; text-align: center;
    padding: 0 14px;
  }
  .back-header .mark { width: 20px; height: 20px; background: var(--brand-blue); margin-bottom: 10px; }
  .back-header .company { font-family: "Michroma", sans-serif; font-size: 17px; color: var(--ink); letter-spacing: .5px; white-space: nowrap; }
  .back-header .tagline { font-family: "Michroma", sans-serif; font-size: 7.5px; letter-spacing: 1px; color: var(--brand-blue); margin-top: 6px; text-transform: uppercase; white-space: nowrap; }
  .back-header-water { top: 140px; }

  .contact { position: absolute; left: 0; right: 0; top: 200px; text-align: center; color: var(--ink); }
  .contact .name { font-family: "Michroma", sans-serif; font-size: 22px; }
  .contact .role { font-family: "Michroma", sans-serif; font-size: 18px; margin-top: 4px; }
  .contact .divider { width: 40px; height: 2px; background: var(--ink); margin: 26px auto; opacity: .7; }
  .contact .line { font-weight: 700; font-size: 17px; line-height: 1.45; }
  .contact .gap { height: 22px; }
</style>
</head>
<body>
  <section class="card card-front" aria-label="Business card front">
    <div class="water" role="img" aria-label="Rippling blue pool water background"></div>
    <div class="front-brand">
      <div class="mark"></div>
      <div class="company">MARLOWE CREST GROUP</div>
      <div class="tagline">Bringing clear water to every pool</div>
    </div>
  </section>

  <section class="card card-back" aria-label="Business card back">
    <div class="water back-header-water" role="img" aria-label="Rippling blue pool water background"></div>
    <header class="back-header">
      <div class="mark"></div>
      <div class="company">MARLOWE CREST GROUP</div>
      <div class="tagline">Bringing clear water to every pool</div>
    </header>
    <div class="contact">
      <div class="name">Darren T. Holt</div>
      <div class="role">CEO</div>
      <div class="divider"></div>
      <div class="line">+1 555 014 2290</div>
      <div class="line">darren@marlowecrest.com</div>
      <div class="gap"></div>
      <div class="line">748 Harbor Lane</div>
      <div class="line">Coral Bay, FL 33090</div>
    </div>
  </section>
</body>
</html>
```